Tall Meadow Business card

We are a company that owns 2 compliance software programs for TV, Radio and Cable industries as well as an online job board. We need a professional business card that incorproates all three logos.

```html
<!DOCTYPE html>
<html lang="en">
<head>
<meta charset="utf-8">
<title>Tall Meadow Business Card</title>
<link rel="stylesheet" href="https://fonts.googleapis.com/css2?family=Montserrat:wght@400;500;600;700&display=swap">
<style>
  :root {
    --page-bg: #f6f6f6;
    --navy: #02254a;
    --brand-blue: #1a7fc6;
    --brand-sky: #2aa3df;
    --ink: #444a52;
    --rule-grey: #8a8f96;
    --card-white: #ffffff;
    --partner-navy: #2a2768;
  }
  * { margin: 0; padding: 0; box-sizing: border-box; }
  html, body { width: 1200px; height: 1000px; overflow: hidden; }
  body {
    background: var(--page-bg);
    font-family: "Montserrat", Arial, sans-serif;
    position: relative;
  }
  .card {
    position: absolute;
    overflow: hidden;
    box-shadow: 0 10px 24px rgba(0,0,0,0.16);
  }
  .card-front {
    left: 273px; top: 99px; width: 653px; height: 372px;
    background: var(--navy);
    display: flex; align-items: center; justify-content: center;
  }
  .wordmark {
    display: flex; align-items: center; gap: 16px;
    color: var(--brand-sky);
    font-weight: 500;
    white-space: nowrap;
  }
  .wordmark-dot {
    border-radius: 50%;
    background: var(--brand-sky);
    flex: none;
  }
  .card-front .wordmark { font-size: 46px; margin-left: -10px; }
  .card-front .wordmark-dot { width: 86px; height: 86px; }

  .card-back {
    left: 271px; top: 524px; width: 657px; height: 375px;
    background: var(--card-white);
  }
  .card-back .wordmark {
    position: absolute; right: 34px; top: 44px;
    font-size: 28px; gap: 10px; color: var(--brand-blue);
  }
  .card-back .wordmark-dot { width: 50px; height: 50px; background: var(--brand-blue); }

  .holder { position: absolute; left: 43px; top: 130px; }
  .holder-name { font-size: 19px; font-weight: 600; color: var(--brand-blue); line-height: 1.1; }
  .holder-role { font-size: 15px; color: var(--ink); margin-top: 4px; }

  .divider { position: absolute; left: 43px; top: 183px; width: 578px; height: 2px; }
  .divider-grey { position: absolute; left: 0; top: 1px; width: 100%; height: 1px; background: var(--rule-grey); }
  .divider-blue { position: absolute; left: 0; top: 0; width: 286px; height: 2px; background: var(--brand-blue); }

  .contacts { position: absolute; left: 43px; top: 193px; list-style: none; }
  .contacts li {
    display: flex; align-items: center; gap: 10px;
    font-size: 16px; color: var(--ink); height: 26px;
    white-space: nowrap;
  }
  .contacts svg { width: 17px; height: 17px; fill: var(--brand-blue); flex: none; }

  .partners { position: absolute; right: 34px; top: 292px; display: flex; gap: 16px; }
  .partner { text-align: right; }
  .partner-name { font-size: 20px; font-weight: 600; color: var(--partner-navy); line-height: 1; white-space: nowrap; }
  .partner-tag { font-size: 7px; font-weight: 600; color: var(--partner-navy); letter-spacing: 0.3px; margin-top: 4px; white-space: nowrap; }
</style>
</head>
<body>
  <section class="card card-front">
    <div class="wordmark"><span class="wordmark-dot"></span><span>Tall Meadow</span></div>
  </section>

  <section class="card card-back">
    <div class="wordmark"><span class="wordmark-dot"></span><span>Tall Meadow</span></div>

    <div class="holder">
      <p class="holder-name">Dana Whitfield</p>
      <p class="holder-role">Owner | CEO</p>
    </div>

    <div class="divider"><span class="divider-grey"></span><span class="divider-blue"></span></div>

    <ul class="contacts">
      <li>
        <svg viewBox="0 0 24 24"><path d="M6.6 10.8c1.4 2.8 3.8 5.1 6.6 6.6l2.2-2.2c.3-.3.7-.4 1-.2 1.1.4 2.3.6 3.6.6.6 0 1 .4 1 1V20c0 .6-.4 1-1 1C10.6 21 3 13.4 3 4c0-.6.4-1 1-1h3.5c.6 0 1 .4 1 1 0 1.3.2 2.5.6 3.6.1.3 0 .7-.2 1z"/></svg>
        <span>555 - 014 - 2288</span>
      </li>
      <li>
        <svg viewBox="0 0 24 24"><path d="M2 5h20L12 12z"/><path d="M2 7l10 7 10-7v12H2z"/></svg>
        <span>hello@tallmeadow.com</span>
      </li>
      <li>
        <svg viewBox="0 0 24 24"><circle cx="12" cy="12" r="10" fill="none" stroke="var(--brand-blue)" stroke-width="2"/><path d="M2 12h20M12 2c3 3 3 17 0 20M12 2c-3 3-3 17 0 20" fill="none" stroke="var(--brand-blue)" stroke-width="1.6"/></svg>
        <span>www.tallmeadow.com</span>
      </li>
    </ul>

    <div class="partners">
      <div class="partner">
        <p class="partner-name">Airwave Check</p>
        <p class="partner-tag">Broadcast Compliance</p>
      </div>
      <div class="partner">
        <p class="partner-name">Line Check</p>
        <p class="partner-tag">MVPD COMPLIANCE</p>
      </div>
    </div>
  </section>
</body>
</html>
```